Brightwater Kinetics (formerly Brightwater Kinetics)

I'm doing a totally different business card now! I recently made some adjustments to my companies moving forward due to outstanding events. Because of this I will be increasing the prize money to the winner and second place.

Here is my new concept.

Brightwater Kinetics
Empowering futures.

My company will be in the following areas:
marketing & innovation, leadership & communication, energy & technology, culture & community, luxury & living.

I do not have a logo - so that is a must! Be creative and you will be rewarded!

I am looking for edgy, big, professional, dynamic!

One idea I had for the logo is a Brightwater symbol (needs to be created) and the shadow of words that describe my business (see above) behind it on one side and then the information on the other.

Go big - go nuts - be creative - YOU ROCK!

Target Market(s)

Multi-billion dollar corporations, world leaders, high end investors, millionaire entrepreneurs

Industry/Entity Type

Leadership

Requirements
Must have
• Name, title, phone, email, website, space for Qr code

Nice to have
• design on front and back. Possible the logo on one side and info on the other.

```html
<!DOCTYPE html>
<html lang="en">
<head>
<meta charset="utf-8">
<title>Brightwater Kinetics Business Card</title>
<link rel="stylesheet" href="https://fonts.googleapis.com/css2?family=Tinos&family=Questrial&family=Carlito&display=swap">
<style>
  :root {
    --backdrop: #e0e0e0;
    --card: #ffffff;
    --band: #b3b3b3;
    --ink-dark: #2b2b2b;
    --ink-logo: #4a4a4a;
    --ink-label: #555555;
    --rule: #555555;
    --band-text: #f4f4f4;
    --qr-frame: #9a9a9a;
  }
  * { box-sizing: border-box; margin: 0; padding: 0; }
  html, body {
    width: 1200px;
    height: 900px;
    overflow: hidden;
    background: var(--backdrop);
  }
  .canvas { position: relative; width: 1200px; height: 900px; }
  .card {
    position: absolute;
    background: var(--card);
    border-radius: 36px;
    overflow: hidden;
    box-shadow: 0 4px 10px rgba(0,0,0,0.18);
  }
  .card--front { left: 40px; top: 50px; width: 650px; height: 390px; }
  .card--back { left: 500px; top: 460px; width: 660px; height: 400px; }
  .wordmark {
    font-family: "Tinos", "Times New Roman", serif;
    font-weight: 400;
    color: var(--ink-logo);
    line-height: 1.05;
    text-align: center;
  }
  .card--front .wordmark {
    position: absolute;
    left: 0; right: 0; top: 150px;
    font-size: 56px;
  }
  .tagline {
    font-family: "Questrial", "Century Gothic", sans-serif;
    font-size: 19px;
    letter-spacing: 0.2px;
  }
  .card--front .tagline {
    position: absolute;
    left: 0; right: 0; top: 240px;
    text-align: center;
    color: var(--ink-dark);
  }
  .band { position: absolute; left: 0; right: 0; background: var(--band); }
  .band--top { top: 0; height: 26px; }
  .band--bottom {
    bottom: 0; height: 62px;
    display: flex; align-items: center; justify-content: center;
  }
  .band--bottom .tagline { color: var(--band-text); font-size: 18px; }
  .card--back .wordmark {
    position: absolute;
    left: 20px; width: 280px; top: 110px;
    font-size: 50px;
  }
  .divider {
    position: absolute;
    left: 312px; top: 56px;
    width: 3px; height: 250px;
    background: var(--rule);
  }
  .contact {
    position: absolute;
    left: 344px; top: 60px;
    font-family: "Carlito", "Calibri", sans-serif;
    color: var(--ink-dark);
  }
  .contact__name { font-size: 29px; font-weight: 400; line-height: 1.1; }
  .contact__title { font-size: 16px; color: var(--ink-label); margin: 2px 0 14px; }
  .contact__list { list-style: none; font-size: 14px; line-height: 1.45; }
  .contact__label { color: var(--ink-label); }
  .qr-space {
    position: absolute;
    left: 344px; top: 240px;
    width: 84px; height: 84px;
    border: 2px solid var(--qr-frame);
    background: var(--card);
  }
</style>
</head>
<body>
  <main class="canvas">
    <section class="card card--front" aria-label="Card front">
      <div class="wordmark">Brightwater Kinetics</div>
      <p class="tagline">Empowering futures through marketing, innovation and leadership</p>
    </section>

    <section class="card card--back" aria-label="Card back">
      <div class="band band--top"></div>
      <div class="wordmark">Brightwater<br>Kinetics</div>
      <div class="divider"></div>
      <div class="contact">
        <h1 class="contact__name">Daniel Reyes</h1>
        <p class="contact__title">Founder &amp; Chief Executive</p>
        <ul class="contact__list">
          <li><span class="contact__label">Email:</span> danielreyes@brightwaterkinetics.com</li>
          <li><span class="contact__label">Website:</span> www.brightwaterkinetics.com.au</li>
          <li><span class="contact__label">Phone Number:</span> (02)7193 528</li>
          <li><span class="contact__label">Mailing Address:</span> 42 Harbour Rd</li>
        </ul>
      </div>
      <div class="qr-space" role="img" aria-label="Space reserved for QR code"></div>
      <div class="band band--bottom">
        <p class="tagline">Empowering futures through marketing, innovation and leadership</p>
      </div>
    </section>
  </main>
</body>
</html>
```